Re-design my Shearing Contract Estimate format.

The one page contract estimate is the output of a Farmer going online to our website and creating their shearing contract estimate.
The design should follow our current branding.
I have uploaded the current contract estimate design and a screen shot of our home page

```html
<!DOCTYPE html>
<html lang="en">
<head>
<meta charset="utf-8">
<title>Shearing Contract Estimate</title>
<link href="https://fonts.googleapis.com/css2?family=Arimo:wght@400;700&display=swap" rel="stylesheet">
<style>
  :root {
    --canvas: #ffffff;
    --sheet: #f3f8f5;
    --sheet-border: #3b5445;
    --brand-dark: #1f5134;
    --brand-green: #40b866;
    --line: #2b3a31;
    --text: #1e2b23;
    --white: #ffffff;
  }
  * { box-sizing: border-box; margin: 0; padding: 0; }
  html, body {
    width: 1200px; height: 1200px; overflow: hidden;
    background: var(--canvas);
    font-family: "Arimo", Arial, sans-serif;
    color: var(--text);
  }
  .estimate-sheet {
    position: absolute; left: 251px; top: 107px;
    width: 698px; height: 987px;
    background: var(--sheet);
    border: 1.5px solid var(--sheet-border);
  }
  .brand {
    position: absolute; left: 0; right: 0; top: 209px; height: 36px;
    display: flex; justify-content: center; align-items: center; gap: 12px;
  }
  .brand-dot {
    width: 26px; height: 26px; border-radius: 50%;
    background: var(--brand-dark);
  }
  .brand-name {
    font-weight: 700; font-size: 30px; line-height: 36px;
    color: var(--brand-dark); letter-spacing: 0.5px;
  }
  .data-table {
    position: absolute; left: 284px; width: 631px;
    border-collapse: collapse; table-layout: fixed;
    font-size: 12.5px;
  }
  .data-table td, .data-table th {
    height: 24px; border: 1.2px solid var(--line);
    padding: 1px 6px 0; vertical-align: middle;
  }
  .data-table .label { text-align: left; }
  .data-table .value { text-align: right; }
  .data-table .strong { font-weight: 700; color: var(--brand-dark); }
  .data-table th {
    background: var(--brand-green); color: var(--white);
    font-weight: 700; text-align: center; height: 25px;
  }
  .contract-table { top: 334px; }
  .contract-table col.key { width: 549px; }
  .sheep-table { top: 407px; }
  .staff-table { top: 647px; }
  .price-table { top: 817px; }
  .split col.key { width: 378px; }
</style>
</head>
<body>
  <main class="estimate-sheet" aria-label="Shearing contract estimate"></main>

  <header class="brand">
    <span class="brand-dot"></span>
    <span class="brand-name">Tallowood Shearing</span>
  </header>

  <table class="data-table contract-table">
    <colgroup><col class="key"><col></colgroup>
    <tr><td class="label strong">Contract No.</td><td class="label">2</td></tr>
    <tr><td class="label strong">Grower Details</td><td></td></tr>
  </table>

  <table class="data-table sheep-table split">
    <colgroup><col class="key"><col></colgroup>
    <tr><th colspan="2">Sheep / Shearing Type</th></tr>
    <tr><td class="label strong">Merinos</td><td class="value">20,000</td></tr>
    <tr><td class="label strong">XB Ewes</td><td class="value">10,000</td></tr>
    <tr><td class="label strong">Lambs</td><td></td></tr>
    <tr><td class="label strong">Full Crutch</td><td></td></tr>
    <tr><td class="label strong">Mkt Crutch</td><td></td></tr>
    <tr><td class="label strong">Rams</td><td></td></tr>
    <tr><td class="label strong">Total Number of Sheep</td><td class="value">30,000</td></tr>
    <tr><td class="label strong">Number of Shed Stands</td><td class="value">8</td></tr>
  </table>

  <table class="data-table staff-table split">
    <colgroup><col class="key"><col></colgroup>
    <tr><th colspan="2">Wool Staff Requirements</th></tr>
    <tr><td class="label">Wool Handler</td><td class="value">3</td></tr>
    <tr><td class="label">Wool Classer</td><td class="value">1</td></tr>
    <tr><td class="label">Wool Presser / Penner (Combined Role)</td><td></td></tr>
    <tr><td class="label">Wool Presser</td><td class="value">0</td></tr>
    <tr><td class="label">Penner</td><td class="value">1</td></tr>
  </table>

  <table class="data-table price-table split">
    <colgroup><col class="key"><col></colgroup>
    <tr><th colspan="2">Estimated Contract Price</th></tr>
    <tr><td class="label">Total Shearing Contract Cost</td><td class="value">$178,458.00</td></tr>
    <tr><td class="label">Total Wool Staff Contract Cost</td><td class="value">$38,745.00</td></tr>
    <tr><td class="label strong">Total Exl GST</td><td class="value">$217,203.00</td></tr>
    <tr><td class="label strong">Total Inc GST</td><td class="value">$238,923.30</td></tr>
    <tr><td class="label">Total Estimated per Sheep</td><td class="value">$7.96</td></tr>
  </table>
</body>
</html>
```